Business Card for Academic Coach

I need a business card designed for me - a private tutor/academic coach.

Glen Marlowe
Academic Coach
AB Velden University, 1994 Cum Laude
Phone: 555-317-8842
glenmmarlowe@quillpost.example

Subjects
SAT and ACT
Math, Physics, Writing

Industry/Entity Type

Business

```html
<!DOCTYPE html>
<html lang="en">
<head>
<meta charset="utf-8">
<title>Glen Marlowe – Private Tutoring</title>
<link rel="stylesheet" href="https://fonts.googleapis.com/css2?family=Open+Sans:ital,wght@0,700;1,700&display=swap">
<style>
  :root {
    --sky-top: #0a80c2;
    --navy-bottom: #020a2e;
    --orange-light: #f8a71e;
    --orange-deep: #f2612e;
    --accent-line: #e8602c;
    --white: #ffffff;
    --stripe-a: #1da3e0;
    --stripe-b: #0a2a5e;
    --stripe-c: #1284c8;
    --stripe-d: #0b3d78;
    --stripe-e: #0f66ac;
    --stripe-f: #0c4a8a;
  }
  html, body {
    margin: 0;
    padding: 0;
    overflow: hidden;
    background: #ffffff;
  }
  .card {
    position: relative;
    width: 1200px;
    height: 686px;
    overflow: hidden;
    background: linear-gradient(180deg, var(--sky-top) 0%, #04457f 45%, var(--navy-bottom) 100%);
    font-family: "Open Sans", Arial, sans-serif;
  }
  .chevron-band,
  .backdrop-emblem {
    position: absolute;
    top: 0;
    left: 0;
  }
  .brand {
    position: absolute;
    left: 318px;
    top: 272px;
    right: 0;
  }
  .brand-name {
    margin: 0;
    padding-left: 2px;
    font-size: 78px;
    font-weight: 700;
    line-height: 1;
    letter-spacing: 1px;
    color: var(--white);
  }
  .brand-rule {
    height: 2px;
    margin-top: 14px;
    background: var(--accent-line);
  }
  .tagline {
    margin: 8px 0 0 -4px;
    font-size: 29px;
    font-style: italic;
    font-weight: 700;
    color: var(--white);
    letter-spacing: 0.3px;
  }
  .tagline .dot {
    color: var(--accent-line);
  }
</style>
</head>
<body>
  <div class="card">
    <svg class="backdrop-emblem" width="1200" height="686" aria-hidden="true">
      <circle cx="760" cy="360" r="300" fill="#ffffff" opacity="0.05"/>
    </svg>

    <svg class="chevron-band" width="260" height="686" aria-hidden="true">
      <defs>
        <linearGradient id="orangeFade" x1="0" y1="0" x2="0" y2="1">
          <stop offset="0" stop-color="var(--orange-light)"/>
          <stop offset="1" stop-color="var(--orange-deep)"/>
        </linearGradient>
        <linearGradient id="shade" x1="0" y1="0" x2="0" y2="1">
          <stop offset="0" stop-color="#000" stop-opacity="0"/>
          <stop offset="1" stop-color="#000" stop-opacity="0.45"/>
        </linearGradient>
      </defs>
      <polygon points="0,0 178,0 213,343 178,686 0,686" fill="var(--stripe-f)"/>
      <polygon points="0,0 160,0 195,343 160,686 0,686" fill="var(--stripe-e)"/>
      <polygon points="0,0 142,0 177,343 142,686 0,686" fill="var(--stripe-d)"/>
      <polygon points="0,0 125,0 160,343 125,686 0,686" fill="var(--stripe-c)"/>
      <polygon points="0,0 108,0 143,343 108,686 0,686" fill="var(--stripe-b)"/>
      <polygon points="0,0 92,0 127,343 92,686 0,686" fill="var(--stripe-a)"/>
      <polygon points="0,0 76,0 111,343 76,686 0,686" fill="var(--stripe-b)"/>
      <polygon points="0,0 64,0 99,343 64,686 0,686" fill="var(--stripe-a)"/>
      <polygon points="0,0 213,0 213,686 0,686" fill="url(#shade)"/>
      <polygon points="0,0 53,0 88,343 53,686 0,686" fill="var(--white)"/>
      <polygon points="0,0 45,0 80,343 45,686 0,686" fill="url(#orangeFade)"/>
    </svg>

    <div class="brand">
      <h1 class="brand-name">Glen Marlowe</h1>
      <div class="brand-rule"></div>
      <p class="tagline">Private Tutoring <span class="dot">•</span> Academic Coach</p>
    </div>
  </div>
</body>
</html>
```